Media and Film Company Needs a New Website

We produce highly stylized commercials and film pieces for our clients. We also produce live events, both corporate and theatrical. Looking for a site that can show off our client videos - have a polished way to show off our team, and be able to create pages to highlight our clients and give a full overview of our project/process with them. We design simple website for some of our clients - so we are very wordpress familiar, and would like something that doesn't feel like a template.

Target Market(s)

content creators, creative directors, production teams, marketing agencies

Industry/Entity Type

Film Production

Number of Pages Required

4 page

Font styles to use
Sans Serif

Requirements
Must have
• slick looking video embed (from YT or Vimeo)
• project pages - client snapshot (what we did for them, how we did it)
• nice landing page, have our company video reel on the page
• testimonials
• contact page
• ability to have photos as a background if we want
Nice to have
• polished clean look - look to our logo colors and linear elements
• we produce very stylized videos for our clients and our website should reflect that
Should not have
• template look or feel to it- please bring your flare to the project!
• take a look at our current site - zantorvo.com we need a better way to highlight our work and our clients

```html
<!DOCTYPE html>
<html lang="en">
<head>
<meta charset="utf-8">
<title>About Zantorvo Media &amp; Entertainment</title>
<link rel="stylesheet" href="https://fonts.googleapis.com/css2?family=Roboto:wght@300;400;500;700;900&family=Roboto+Condensed:wght@400&display=swap">
<style>
:root{
  --pink:#e0157a;
  --blue:#2a8fc9;
  --accent-red:#e8441b;
  --ink:#333;
  --nav-bg:#0b0b0b;
  --footer-bg:#1d1d1d;
  --band-blue:#dff0fb;
}
*{margin:0;padding:0;box-sizing:border-box}
html,body{width:808px;height:1200px;overflow:hidden;background:#fff}
body{position:relative;font-family:'Roboto',sans-serif;color:var(--ink)}
.abs{position:absolute}

/* nav */
.top-nav{left:0;top:0;width:808px;height:24px;background:var(--nav-bg);display:flex;justify-content:center}
.top-nav a{color:#eee;font-size:7.5px;text-decoration:none;line-height:24px;padding:0 36px;border-right:1px solid #2a2a2a;letter-spacing:.2px}
.top-nav a:last-child{border-right:none}

/* hero */
.hero{left:0;top:24px;width:808px;height:197px;background:radial-gradient(ellipse at 50% 55%,#6a6a6a 0%,#3d3d3d 45%,#1c1c1c 100%)}
.brand{left:0;top:110px;width:808px;text-align:center;color:#fff;font-weight:500;font-size:17px;letter-spacing:2px}

/* clients */
.clients{left:109px;top:258px;width:170px;height:277px;border-left:2px solid var(--accent-red)}
.clients h2{background:#f3f3f3;width:156px;height:27px;padding-left:11px;font-family:'Roboto Condensed',sans-serif;font-weight:400;font-size:20px;color:var(--pink);line-height:30px}
.clients ul{list-style:none;margin:5px 0 0 11px}
.clients li{font-size:7px;color:#555;height:14.7px;line-height:14px;width:142px;border-bottom:1px dotted #ccc;padding-left:11px;position:relative;white-space:nowrap}
.clients li:last-child{border-bottom:none}
.clients li::before{content:"";position:absolute;left:0;top:4px;width:5px;height:5px;border:1.4px solid var(--accent-red);border-radius:50%}
.divider{left:305px;top:280px;width:1px;height:250px;background:#ececec}

/* about */
.about-title{left:333px;top:254px;font-size:27px;font-weight:700;color:var(--pink)}
.about-sub{left:333px;top:287px;font-size:12px;color:var(--blue)}
.about-rule{left:333px;top:309px;width:361px;height:2px;background:var(--pink);box-shadow:0 2px 0 #f4c3dc}
.about-photo{left:333px;top:333px;width:185px;height:122px;border:3px solid #111;padding:4px;background:#fff}
.about-photo div{width:100%;height:100%;background:linear-gradient(135deg,#3a1a10 0%,#8b4a22 40%,#2a1812 75%,#c07a3a 100%)}
.about-text{font-size:7px;line-height:11.2px;color:#444}
.about-text p+p{margin-top:6px}

/* call band */
.call-band{left:0;top:579px;width:808px;height:79px;background:var(--band-blue);text-align:center}
.call-band .lead{font-size:21px;font-weight:300;color:#222;margin-top:14px;line-height:24px}
.call-band .ask{font-size:24px;font-weight:900;color:var(--pink);line-height:28px;letter-spacing:-.3px}

/* showcase */
.showcase{left:0;top:658px;width:808px;height:356px;background:radial-gradient(ellipse at 50% 70%,#f08bbd 0%,#e0539b 45%,#c8387f 100%)}
.showcase-frame{left:109px;top:698px;width:590px;height:280px;background:#fff;padding:6px}
.video-still{position:relative;width:100%;height:100%;overflow:hidden;
  background:
    linear-gradient(180deg,rgba(0,0,0,0) 0%,rgba(0,0,0,0) 78%,#4a4a4a 86%,#2b2b2b 100%),
    linear-gradient(90deg,#2c2c2c 0%,#6d6d6d 8%,#b9b9b9 17%,#f4f4f4 30%,#fafafa 55%,#e9e9e9 62%,#5a5a5a 72%,#1f1f1f 84%,#3b3b3b 100%)}
.play{position:absolute;left:50%;top:50%;width:58px;height:58px;margin:-29px 0 0 -29px;border-radius:50%;background:rgba(224,21,122,.9);box-shadow:0 0 0 5px rgba(255,255,255,.55)}
.play svg{display:block}
.video-bar{position:absolute;left:0;bottom:0;width:100%;height:22px;background:rgba(0,0,0,.55);display:flex;align-items:center;padding:0 10px;gap:9px}
.video-bar .track{flex:1;height:3px;background:rgba(255,255,255,.35);position:relative}
.video-bar .track::before{content:"";position:absolute;left:0;top:0;width:18%;height:3px;background:var(--pink)}
.video-bar .time{font-size:7px;color:#fff}

/* partners */
.partners{left:0;top:1014px;width:808px;height:95px;background:#fff}
.partner{top:1056px;width:100px;margin-left:-50px;text-align:center;font-size:11px;font-weight:500;color:#444}
.arrow{top:1054px;width:23px;height:23px;border-radius:50%;background:#c9c9c9}
.arrow svg{display:block}

/* footer */
.footer{left:0;top:1109px;width:808px;height:91px;background:var(--footer-bg);text-align:center}
.footer-nav{margin-top:22px;font-size:7px;color:#ddd;letter-spacing:.2px}
.footer-nav span{margin:0 5px;color:#999}
.copyright{margin-top:8px;font-size:6.5px;color:#999}
.social{display:flex;justify-content:center;gap:4.6px;margin-top:12px}
.social i{display:block;width:15px;height:15px;border-radius:50%;background:#3a3a3a}
</style>
</head>
<body>

<nav class="abs top-nav">
  <a href="#">HOME</a><a href="#">PORTFOLIO</a><a href="#">ABOUT ZANTORVO</a><a href="#">TESTIMONIALS</a><a href="#">PRESS</a><a href="#">CONTACT US</a>
</nav>

<header class="abs hero" role="img" aria-label="Black and white aerial view of a city skyline"></header>
<div class="abs brand">ZANTORVO MEDIA &amp; ENTERTAINMENT</div>

<aside class="abs clients">
  <h2>Our Clients:</h2>
  <ul>
    <li>RIVERMARK DOCS FESTIVAL</li>
    <li>QUELLIN GROUP</li>
    <li>BREVIX TECH</li>
    <li>LARKSPAN EVENTS</li>
    <li>HALDEN MUSIC</li>
    <li>BRIGHT PATHS WELLNESS</li>
    <li>OAKFOLD FILMWORKS</li>
    <li>THE MARLOWE ACADEMY</li>
    <li>PEBBLECORE</li>
    <li>CORVANA FOODS</li>
    <li>FIELDLIGHT FILM FESTIVAL</li>
    <li>TORREN HERITAGE FOUNDATION</li>
    <li>ALDER COMMUNITY RESOURCES</li>
    <li>SAFFRA COOKING SCHOOL</li>
    <li>IRONWAY FITNESS CONCEPTS</li>
    <li>VELTO GUILD</li>
    <li>NUVRA</li>
  </ul>
</aside>
<div class="abs divider"></div>

<h1 class="abs about-title">ABOUT ZANTORVO</h1>
<div class="abs about-sub">THE ZANTORVO DIFFERENCE WHO WE ARE</div>
<div class="abs about-rule"></div>
<div class="abs about-photo"><div role="img" aria-label="Film scene of actors seated at a warmly lit bar"></div></div>
<div class="abs about-text" style="left:523px;top:331px;width:178px">
  <p>Zantorvo Media &amp; Entertainment provides full-service campaigns in film and media production, live entertainment &amp; theatrical production, marketing &amp; advertising, and event management in the DC metro area.</p>
  <p>Founded in 2009, Zantorvo Media &amp; Entertainment has built a reputation working for clients including the Meridian Film Institute, Quellin Group, Halden Music, Alder Community Resources, and Larkspan Events.</p>
</div>
<div class="abs about-text" style="left:333px;top:471px;width:368px">
  <p>Zantorvo Media &amp; Entertainment works to build strong relationships with its clients through full-service campaigns in multiple industries. Through community outreach, Zantorvo develops its campaigns thoroughly to provide the most successful services to its clients.</p>
</div>

<section class="abs call-band">
  <p class="lead">THE CHAIR IS OPEN...</p>
  <p class="ask">HOW CAN WE HELP YOU TELL YOUR STORY?</p>
</section>

<section class="abs showcase" role="img" aria-label="Pink backdrop with soft glowing light spots"></section>
<div class="abs showcase-frame">
  <div class="video-still" role="img" aria-label="Company video reel: studio set with an empty chair on a white backdrop, lights, boom microphone and camera">
    <a class="play" href="#" aria-label="Play video reel"><svg width="58" height="58" viewBox="0 0 58 58"><path d="M23 18v22l18-11z" fill="#fff"/></svg></a>
    <div class="video-bar">
      <svg width="8" height="9" viewBox="0 0 8 9"><path d="M0 0v9l8-4.5z" fill="#fff"/></svg>
      <div class="track"></div>
      <span class="time">0:42 / 3:58</span>
    </div>
  </div>
</div>

<section class="abs partners"></section>
<div class="abs arrow" style="left:68px"><svg width="23" height="23" viewBox="0 0 23 23"><path d="M13 7.5 9 11.5l4 4" fill="none" stroke="#fff" stroke-width="1.5"/></svg></div>
<div class="abs arrow" style="left:718px"><svg width="23" height="23" viewBox="0 0 23 23"><path d="M10 7.5l4 4-4 4" fill="none" stroke="#fff" stroke-width="1.5"/></svg></div>
<div class="abs partner" style="left:142px">Rivermark Docs</div>
<div class="abs partner" style="left:251px">Alder Resources</div>
<div class="abs partner" style="left:361px">Halden Music</div>
<div class="abs partner" style="left:469px">Pebblecore</div>
<div class="abs partner" style="left:582px">Brevix Tech</div>
<div class="abs partner" style="left:676px">Quellin Group</div>

<footer class="abs footer">
  <div class="footer-nav">HOME<span>|</span>PORTFOLIO<span>|</span>ABOUT ZANTORVO<span>|</span>TESTIMONIALS<span>|</span>PRESS<span>|</span>CONTACT US</div>
  <div class="copyright">Copyright © 2017. zantorvo.com | Privacy policy</div>
  <div class="social"><i></i><i></i><i></i><i></i><i></i><i></i></div>
</footer>

</body>
</html>
```